Business Card Design Project - IT Company

CLOUD IT company working with medium to large corporate clients requires 2 sided Business Card design.

Strong, Professional and modern is what I am looking for.

The Logo JPG attached has all the colour palette options. which consist of Red and Silver on various backgrounds

Preferred option for the Back of card is either Silver Text on Red or Silver Text on Black. Though this is not concrete. Surprise me.

Logo must be prominent along with Contact details of the staff member

Tagline can be all Capitals " CLOUD MANAGED SERVICES"

I will look to provide feedback and tweaks to get the right design so it should be a fun process.

I will provide the layered files to the top few contenders.

Reason: Leaving the door open for some creativity. Don't forget this is an technology company. .

Target Market(s)

Leaders, decision makers, CEOs, CIOs,

Industry/Entity Type

Business

Requirements
Must have
• Data must have is

Company Name: Velquora
Tagline: Cloud Managed Services

No Particular order

First Name Last name
Director
Mobile 0452 987 654
www.velquora.com
First.Lastname@velquora.com
Suite 5, 48 Marlowe Lane, Sydney NSW 2000

```html
<!DOCTYPE html>
<html lang="en">
<head>
<meta charset="utf-8">
<title>Velquora – Business Card</title>
<link rel="stylesheet" href="https://fonts.googleapis.com/css2?family=PT+Sans:wght@400;700&family=PT+Sans+Narrow:wght@400;700&display=swap">
<style>
  :root {
    --page: #e7e4e0;
    --card-white: #f1f1f1;
    --brand-red: #a11d25;
    --brand-grey: #5c5d60;
    --brand-black: #141414;
    --ink: #2b2b2b;
    --silver: #d9d9d9;
  }
  * { margin: 0; padding: 0; box-sizing: border-box; }
  html, body {
    width: 1200px; height: 1024px; overflow: hidden;
    background: var(--page);
    font-family: "PT Sans", Arial, sans-serif;
  }
  .sheet {
    position: relative; width: 1200px; height: 1024px;
    display: flex; flex-direction: column; align-items: center; justify-content: center; gap: 40px;
  }
  .card {
    position: relative; width: 760px; height: 464px; overflow: hidden;
    box-shadow: 0 6px 18px rgba(0,0,0,0.18);
  }

  /* Front */
  .card-front { background: var(--card-white); }
  .front-edge { position: absolute; inset: 0; }
  .brand {
    position: absolute; left: 64px; top: 150px;
    display: flex; align-items: center; gap: 18px;
  }
  .brand-dot { width: 46px; height: 46px; border-radius: 50%; background: var(--brand-red); }
  .brand-name {
    font-family: "PT Sans", Arial, sans-serif; font-weight: 700;
    font-size: 64px; line-height: 1; color: var(--ink); letter-spacing: -0.5px;
  }
  .brand-tagline {
    position: absolute; left: 194px; top: 222px;
    font-family: "PT Sans Narrow", Arial, sans-serif;
    font-size: 12px; letter-spacing: 1.2px; color: var(--ink);
  }
  .contact {
    position: absolute; left: 196px; top: 292px;
    font-family: "PT Sans Narrow", Arial, sans-serif; font-size: 20px; line-height: 28px; color: var(--ink);
    list-style: none;
  }
  .contact-label { color: var(--brand-red); margin-right: 4px; }
  .contact-address { margin-top: 6px; }
  .person {
    position: absolute; left: 470px; top: 62px;
    padding-left: 10px; border-left: 1px solid var(--ink);
    font-family: "PT Sans Narrow", Arial, sans-serif;
  }
  .person-name { font-size: 26px; line-height: 28px; color: var(--brand-red); letter-spacing: 0.5px; }
  .person-role { font-size: 18px; line-height: 22px; color: var(--ink); }

  /* Back */
  .card-back { background: var(--brand-red); }
  .back-bands { position: absolute; inset: 0; }
  .back-name {
    position: absolute; left: 0; right: 0; top: 178px; text-align: center;
    font-family: "PT Sans", Arial, sans-serif; font-weight: 700;
    font-size: 76px; line-height: 1; color: var(--silver);
  }
  .back-tagline {
    position: absolute; left: 0; right: 0; top: 266px; text-align: center;
    font-family: "PT Sans Narrow", Arial, sans-serif;
    font-size: 16px; letter-spacing: 3px; color: var(--silver);
  }
</style>
</head>
<body>
<main class="sheet">

  <section class="card card-front" aria-label="Front of business card">
    <svg class="front-edge" width="760" height="464" viewBox="0 0 760 464" aria-hidden="true">
      <rect x="722" y="0" width="38" height="120" fill="var(--brand-grey)"/>
      <polygon points="600,464 722,300 760,300 760,464" fill="var(--brand-red)"/>
      <line x1="596" y1="464" x2="718" y2="300" stroke="#ffffff" stroke-width="3"/>
      <rect x="0" y="452" width="760" height="12" fill="var(--brand-black)"/>
    </svg>

    <div class="brand">
      <span class="brand-dot" aria-hidden="true"></span>
      <span class="brand-name">Velquora</span>
    </div>
    <div class="brand-tagline">CLOUD MANAGED SERVICES</div>

    <div class="person">
      <div class="person-name">RHIANNON CASTELL</div>
      <div class="person-role">Director</div>
    </div>

    <ul class="contact">
      <li><span class="contact-label">M:</span>0452 987 654</li>
      <li><span class="contact-label">E:</span>rcastell@velquora.com</li>
      <li><span class="contact-label">W:</span>www.velquora.com</li>
      <li class="contact-address">Suite 5, 48 Marlowe Lane, Sydney NSW 2000</li>
    </ul>
  </section>

  <section class="card card-back" aria-label="Back of business card">
    <svg class="back-bands" width="760" height="464" viewBox="0 0 760 464" aria-hidden="true">
      <polygon points="0,0 150,0 70,464 0,464" fill="var(--brand-grey)"/>
      <line x1="150" y1="0" x2="70" y2="464" stroke="#ffffff" stroke-width="4"/>
      <polygon points="640,0 760,0 760,464 560,464" fill="var(--brand-black)"/>
      <line x1="640" y1="0" x2="560" y2="464" stroke="#ffffff" stroke-width="4"/>
    </svg>
    <div class="back-name">Velquora</div>
    <div class="back-tagline">CLOUD MANAGED SERVICES</div>
  </section>

</main>
</body>
</html>
```